Mental Health Therapy Website

I need a design for a mental health therapy website. It is a private practice. The business name is Brindle Counseling, PLLC. My name is Martin Hale, LMHC, NCC, DCC. I would like some of the features/menus to be Home; Welcome/About Me, Rates and Services, Common Questions, and Contact.
If possible I would like a blog on the main page that I can update with articles I write. I would like the contact page to feature a map to my location (4318 Cedarbend Ave. E, Lakewood, WA 98499).
I would like to place a small photo of me on the Welcome/About page.
I am new to this so if I am forgetting anything, please ask me!!
I will upload my logo so you can fit it and the color scheme into the design.
Thank you so very much!

```html
<!DOCTYPE html>
<html lang="en">
<head>
<meta charset="utf-8">
<title>Brindle Counseling</title>
<link href="https://fonts.googleapis.com/css2?family=Arimo:wght@400;700&display=swap" rel="stylesheet">
<style>
:root{
  --green:#6f9a4f;
  --green-dark:#5d8741;
  --green-btn:#6d9a3c;
  --logo-blue:#2d6aa0;
  --ink:#1e1e1e;
  --text:#333333;
  --muted:#9a9a9a;
  --line:#d9d9d9;
  --page-top:#ececee;
  --footer:#232323;
  --footer-text:#c9c9c9;
  --icon-grey:#6e6e6e;
}
*{margin:0;padding:0;box-sizing:border-box}
html,body{width:1070px;height:1200px;overflow:hidden}
body{position:relative;background:#fff;font-family:"Arimo",Arial,sans-serif;color:var(--text)}
.top-band{position:absolute;left:0;top:0;width:1070px;height:446px;background:linear-gradient(#f3f3f5,#e7e7ea);border-bottom:2px solid #dcdcdc}
.abs{position:absolute}
.brand{left:90px;top:26px;display:flex;align-items:center;gap:10px}
.brand-mark{width:46px;height:46px;border-radius:50%;background:var(--green)}
.brand-name{font-size:30px;color:var(--logo-blue);font-weight:400;letter-spacing:.5px}
.contact-top{top:40px;display:flex;align-items:center;gap:11px;font-size:11px;color:var(--ink)}
.round-icon{width:27px;height:27px;border-radius:50%;background:var(--icon-grey);display:flex;align-items:center;justify-content:center}
.nav{left:90px;top:99px;width:892px;height:42px;background:var(--green);display:flex;align-items:center}
.nav a{color:#1d1d1d;text-decoration:none;font-size:13px;height:100%;display:flex;align-items:center;padding:0 23px 0 28px;border-right:1px solid var(--green-dark)}
.nav a:first-child{padding-left:29px}
.nav a:nth-child(5){border-right:none}
.nav .search{position:absolute;right:18px;top:11px}
.slider{left:90px;top:141px;width:892px;height:307px;background:radial-gradient(ellipse at 50% 55%,#6f8a3a 0%,#c07d55 30%,#3b2a22 62%,#1c1c1f 100%)}
.slide-arrow{top:275px;width:22px;height:30px;background:#9a9a9a;display:flex;align-items:center;justify-content:center}
.dots{left:479px;top:422px;width:112px;height:24px;background:rgba(235,235,235,.85);border-radius:6px 6px 0 0;display:flex;justify-content:center;align-items:center;gap:6px}
.dots i{width:11px;height:11px;border-radius:50%;background:#8d8d8d;display:block}
.dots i.on{background:#2d5d9a}
.portrait{left:90px;top:486px;width:135px;height:95px;background:linear-gradient(135deg,#e9e9ee,#c59b82 55%,#2a2a2e)}
.welcome{left:247px;top:490px;width:725px}
.welcome h1{font-size:16px;font-weight:400;color:var(--ink);margin-bottom:9px}
.welcome p{font-size:10px;line-height:19.6px;color:var(--text);height:59px;overflow:hidden}
.card{top:608px;width:285px;height:225px;background:#fff;box-shadow:0 0 6px rgba(0,0,0,.12);text-align:center;overflow:hidden}
.card .ico{height:94px;display:flex;align-items:flex-end;justify-content:center;padding-bottom:6px}
.card h2{font-size:16px;font-weight:400;color:var(--ink);margin:3px 0 10px}
.card p{font-size:10px;line-height:19.6px;padding:0 14px}
.card .corner{position:absolute;right:0;bottom:0}
.section-title{font-size:16px;color:var(--ink);font-weight:400}
.rule{height:1px;background:var(--line)}
.article{left:90px;top:910px;width:589px;height:165px;background:#fbfbfb;box-shadow:0 0 4px rgba(0,0,0,.08)}
.avatar{left:24px;top:19px;width:128px;height:128px;border-radius:50%;background:#e3e3e3;padding:9px}
.avatar div{width:100%;height:100%;border-radius:50%;background:linear-gradient(150deg,#b8c7d4,#c99a7d 55%,#2d3340)}
.article .mini-dots{right:8px;top:14px;display:flex;gap:5px}
.mini-dots i{width:9px;height:9px;border-radius:50%;background:#dedede;display:block}
.article .body{left:180px;top:38px;width:390px;font-size:10px;line-height:19.6px;color:var(--ink)}
.article .quote{text-align:justify}
.article .meta{margin-top:6px}
.article .who{margin-top:4px;line-height:19px}
.appt{left:695px;top:870px;width:286px;font-size:10px;color:var(--ink)}
.appt .row{display:flex;align-items:center;gap:14px;height:20px}
.appt p{line-height:19.6px;text-align:justify}
.btn{display:inline-block;background:var(--green-btn);color:#1a1a1a;font-size:15px;padding:5px 19px;margin-top:13px}
.footer{left:0;top:1108px;width:1070px;height:92px;background:var(--footer);color:var(--footer-text);font-size:10px}
.footer .links{position:absolute;left:91px;top:26px}
.footer .copy{position:absolute;left:89px;top:53px}
.social{position:absolute;right:87px;top:31px;display:flex;gap:9px}
.social i{width:28px;height:28px;border-radius:50%;background:#5a5a5a;display:block}
</style>
</head>
<body>
<div class="top-band"></div>

<div class="abs brand"><span class="brand-mark"></span><span class="brand-name">Brindle Counseling</span></div>

<div class="abs contact-top" style="left:644px">
  <span class="round-icon"><svg width="14" height="12" viewBox="0 0 14 12"><path d="M1 4c0-3 12-3 12 0l-2 1-1-2H4L3 5zM3 6h8l1 5H2z" fill="#fff"/></svg></span>
  <span>Call Us : 1800-5127-6630</span>
</div>
<div class="abs contact-top" style="left:831px">
  <span class="round-icon"><svg width="13" height="10" viewBox="0 0 13 10"><rect x=".5" y=".5" width="12" height="9" fill="none" stroke="#fff"/><path d="M.5.5l6 5 6-5" fill="none" stroke="#fff"/></svg></span>
  <span>info@brindlecare.com</span>
</div>

<nav class="abs nav">
  <a>Home</a><a>About Me</a><a>Rates and Services</a><a>Common Questions</a><a>Contact</a>
  <svg class="search" width="22" height="22" viewBox="0 0 22 22"><circle cx="9" cy="9" r="7" fill="none" stroke="#333" stroke-width="1.3"/><path d="M14 14l7 7" stroke="#333" stroke-width="1.5"/></svg>
</nav>

<div class="abs slider" role="img" aria-label="Two cupped hands protecting a young green seedling"></div>
<div class="abs slide-arrow" style="left:90px"><svg width="8" height="12"><path d="M7 1L2 6l5 5" fill="none" stroke="#fff" stroke-width="2"/></svg></div>
<div class="abs slide-arrow" style="left:960px"><svg width="8" height="12"><path d="M1 1l5 5-5 5" fill="none" stroke="#fff" stroke-width="2"/></svg></div>
<div class="abs dots"><i></i><i></i><i class="on"></i><i></i><i></i><i></i></div>

<div class="abs portrait" role="img" aria-label="Portrait photo of the therapist"></div>
<section class="abs welcome">
  <h1>Welcome To Our Company</h1>
  <p>Mental health counseling/therapy for individuals (children, adolescents, adults), couples, and families.&nbsp; I am a trauma certified therapist that utilizes CBT+ to assist with trauma. My approach to therapy is psychodynamic that utilizes tools from CBT, Solutions focused, Emotionsfocused, and Psychoeducation therapies to assist clients managing depression, anxiety, truama, phobias, personality disorders, ADHD, selfinjury,and communication issues.&nbsp; Sessions</p>
</section>

<div class="abs card" style="left:90px">
  <div class="ico"><svg width="46" height="80" viewBox="0 0 46 80"><path d="M23 0C10 0 0 10 0 23c0 12 9 18 11 30v4h24v-4c2-12 11-18 11-30C46 10 36 0 23 0z" fill="var(--green)"/><rect x="11" y="60" width="24" height="4" fill="var(--green)"/><rect x="11" y="67" width="24" height="4" fill="var(--green)"/><rect x="13" y="74" width="20" height="4" fill="var(--green)"/></svg></div>
  <h2>24 Hours Service</h2>
  <p>Mental health counseling/therapy for individuals (children, adolescents, adults), couples,and families.&nbsp; I am a trauma certified therapist that utilizes CBT+ to assist with trauma.</p>
  <svg class="corner" width="38" height="30"><path d="M38 0v30H0z" fill="var(--green)"/><circle cx="29" cy="21" r="5" fill="none" stroke="#fff"/><path d="M29 18v6M26 21h6" stroke="#fff"/></svg>
</div>
<div class="abs card" style="left:394px">
  <div class="ico"><svg width="76" height="76" viewBox="0 0 76 76"><circle cx="38" cy="38" r="37" fill="#f1f1f1"/><circle cx="38" cy="38" r="20" fill="var(--green)"/></svg></div>
  <h2>Psychoeducation therapies</h2>
  <p>Mental health counseling/therapy for individuals (children, adolescents, adults), couples,and families.&nbsp; I am a trauma certified therapist that utilizes CBT+ to assist with trauma.</p>
  <svg class="corner" width="38" height="30"><path d="M38 0v30H0z" fill="var(--green)"/><circle cx="29" cy="21" r="5" fill="none" stroke="#fff"/><path d="M29 18v6M26 21h6" stroke="#fff"/></svg>
</div>
<div class="abs card" style="left:696px">
  <div class="ico"><svg width="74" height="74" viewBox="0 0 74 74"><circle cx="37" cy="37" r="37" fill="var(--green)"/><path d="M31 13h12v18h18v12H43v18H31V43H13V31h18z" fill="#fff"/></svg></div>
  <h2>Health Counseling/Therapy</h2>
  <p>Mental health counseling/therapy for individuals (children, adolescents, adults), couples,and families.&nbsp; I am a trauma certified therapist that utilizes CBT+ to assist with trauma.</p>
  <svg class="corner" width="38" height="30"><path d="M38 0v30H0z" fill="var(--green)"/><circle cx="29" cy="21" r="5" fill="none" stroke="#fff"/><path d="M29 18v6M26 21h6" stroke="#fff"/></svg>
</div>

<h3 class="abs section-title" style="left:89px;top:867px">Latest Articles</h3>
<div class="abs rule" style="left:89px;top:894px;width:286px"></div>

<article class="abs article">
  <div class="abs avatar"><div role="img" aria-label="Photo of the article author"></div></div>
  <div class="abs mini-dots"><i></i><i></i><i></i><i></i></div>
  <div class="abs body">
    <p class="quote">" There are many variations passages of Lorem Ipsum available, but the majority have suffered alteration in some form, by injected randomise words which don't look even believable. "</p>
    <p class="meta">By: admin | Tags: Graphic, illustration, Logo</p>
    <p class="who">- Leo Fenwick<br>customer</p>
  </div>
</article>

<section class="abs appt">
  <h3 class="section-title">Make an Appointment</h3>
  <div class="rule" style="margin:10px 0 14px"></div>
  <div class="row"><svg width="14" height="11" viewBox="0 0 14 12"><path d="M1 4c0-3 12-3 12 0l-2 1-1-2H4L3 5zM3 6h8l1 5H2z" fill="#333"/></svg>1800-5127-6600</div>
  <div class="row" style="margin-top:14px"><svg width="14" height="10" viewBox="0 0 13 10"><rect x=".5" y=".5" width="12" height="9" fill="none" stroke="#333"/><path d="M.5.5l6 5 6-5" fill="none" stroke="#333"/></svg>hello@brindlecare.com</div>
  <p style="margin-top:11px">Lorem ipsum dolor sit amet, consectetur adipiscing elit. Etiam quis placerat urna. Nulla nulla diam, adipiscing non ornare non, commodo</p>
  <span class="btn">Contact Form</span>
</section>

<footer class="abs footer">
  <div class="links">Sitemap | Terms of Use | Privacy Policy</div>
  <div class="copy">© 2014. Mental Health therapy clinic. All rights reserved.</div>
  <div class="social"><i></i><i></i><i></i><i></i><i></i></div>
</footer>
</body>
</html>
```